re brand of safeguardly.pro to Vexawatch.co.uk

We would like a new site design for our safeguardly.pro site

the new domain is Vexawatch.co.uk

we like the blue colour smiler to this site http://www.fundsentrypal.co.uk, and we would like real images o people using instead of cartons

you can take inspiration from the credit ref agency monthly membership site but this product is not a credit report we just like that look

https://www.loanharbor.co.uk
http://www.fundsentrypal.co.uk/
https://www.brimzo.co.uk/

Reason: we have added more details to the project brief and also increased the budget and committed to buying a design

We have guaranteed the project extend the dead line and increased the payment we have also added more details in the brief to give you guys more direction I am looking forward to seeing the designs

Target Market(s)

18 to 50 yo concerned with the privacy and id fraud

The bulk of clients our aged 18 to 30 so a fresh feel is important

Industry/Entity Type

Domain

Colors
33a6d7
0592cd
0555a3
3176b5
85cae6

```html
<!DOCTYPE html>
<html lang="en">
<head>
<meta charset="utf-8">
<title>Vexawatch</title>
<link href="https://fonts.googleapis.com/css2?family=Open+Sans:wght@400;600;700&display=swap" rel="stylesheet">
<style>
:root{
  --blue-dark:#0555a3;
  --blue-mid:#3176b5;
  --blue:#0592cd;
  --blue-bright:#33a6d7;
  --blue-pale:#85cae6;
  --ink:#333c46;
  --muted:#6f7780;
  --grey-bg:#eef1f4;
  --white:#ffffff;
}
*{box-sizing:border-box;margin:0;padding:0}
html,body{width:781px;height:1200px;overflow:hidden}
body{font-family:"Open Sans",Arial,sans-serif;color:var(--ink);background:var(--white)}
.page{width:781px;height:1200px;position:relative;overflow:hidden}

/* header */
.site-header{height:40px;background:var(--blue-dark);display:flex;align-items:center;justify-content:space-between;padding:0 26px}
.brand{display:flex;align-items:center;gap:8px;color:var(--white);font-weight:700;font-size:17px;letter-spacing:.5px}
.brand-dot{width:18px;height:18px;border-radius:50%;background:var(--blue-bright)}
.main-nav{display:flex;align-items:center;gap:14px}
.main-nav a{color:var(--white);text-decoration:none;font-size:7.5px;font-weight:600;letter-spacing:.4px}
.main-nav .login{border:1px solid var(--blue-pale);background:var(--blue-bright);padding:5px 9px;border-radius:2px}

/* hero */
.hero{height:265px;position:relative;background:linear-gradient(180deg,#1f95d3 0%,#0a78c2 100%);overflow:hidden}
.hero-copy{position:absolute;left:40px;top:30px;width:340px;color:var(--white)}
.hero-copy h1{font-size:44px;font-weight:700;letter-spacing:1px;line-height:1}
.hero-list{list-style:none;margin-top:16px}
.hero-list li{display:flex;gap:9px;font-size:15px;line-height:1.25;margin-bottom:8px}
.hero-list svg{flex:none;margin-top:2px}
.hero-cta{display:inline-block;margin-top:10px;background:var(--blue-pale);color:var(--white);font-size:15px;font-weight:600;padding:8px 16px;border-radius:3px;border:1px solid rgba(255,255,255,.5)}
.hero-media{position:absolute;right:38px;top:22px;width:330px;height:228px;border-radius:6px;background:linear-gradient(160deg,#dfe9f2 0%,#9fc2dc 60%,#5d8fb8 100%);border:6px solid #2a3440}
.slider-dots{position:absolute;left:40px;bottom:14px;display:flex;gap:6px}
.slider-dots span{width:9px;height:9px;border-radius:50%;background:rgba(255,255,255,.55)}
.slider-dots span:first-child{background:var(--white)}

/* welcome */
.welcome{height:90px;padding:14px 40px 0}
.section-title{color:var(--blue-dark);font-size:14px;font-weight:700;letter-spacing:.3px}
.welcome p{margin-top:7px;font-size:8px;line-height:1.5;color:var(--muted)}

/* what we do / news */
.split{height:230px;background:var(--grey-bg);display:flex;gap:30px;padding:24px 40px 0}
.split-col{flex:1}
.split-col .section-title{font-size:16px;padding-bottom:6px;border-bottom:1px solid #cfd6dd}
.what-body{display:flex;gap:12px;margin-top:12px}
.what-media{width:118px;height:92px;flex:none;background:linear-gradient(135deg,#4a5664,#1e2a36)}
.small-text{font-size:8px;line-height:1.5;color:var(--muted)}
.btn-small{display:inline-block;margin-top:12px;background:var(--blue);color:var(--white);font-size:7px;font-weight:600;padding:6px 12px;border-radius:2px}
.news-item{margin-top:12px}
.news-item .read{display:block;color:var(--blue);font-size:8px;font-weight:600;margin-top:2px}

/* why */
.why{height:235px;padding-top:22px;text-align:center}
.why .section-title{font-size:15px;color:var(--blue-dark)}
.features{display:flex;justify-content:center;gap:38px;margin-top:22px}
.feature{width:120px}
.feature-box{width:78px;height:78px;margin:0 auto;background:var(--blue);border-radius:3px;display:flex;align-items:center;justify-content:center}
.feature h3{margin-top:10px;font-size:9.5px;font-weight:700;color:var(--blue-dark);line-height:1.3}

/* signup */
.signup{height:150px;background:var(--grey-bg);padding-top:22px;text-align:center}
.signup .section-title{font-size:15px}
.signup-form{display:flex;gap:14px;justify-content:center;margin-top:18px}
.field{width:222px;height:28px;background:var(--white);border:1px solid #d6dce2;font-size:8px;color:#9aa2aa;text-align:left;padding:9px 10px}
.submit{display:inline-block;margin-top:12px;width:196px;background:var(--blue);color:var(--white);font-size:14px;font-weight:600;padding:6px 0;border-radius:2px}

/* footer */
.site-footer{height:190px;background:var(--blue-dark);color:#cfe3f3;padding:22px 40px 0;text-align:center;position:relative}
.footer-copy{font-size:8px}
.footer-links{font-size:8px;margin-top:5px;color:var(--white)}
.footer-terms{margin-top:20px;font-size:7px;line-height:1.55;text-align:left;color:#a9c7e2}
.footer-bottom{position:absolute;left:40px;right:40px;bottom:18px;display:flex;justify-content:space-between;align-items:center}
.social{display:flex;gap:6px}
.social span{width:18px;height:18px;border-radius:50%;background:var(--blue-bright)}
.payments{display:flex;gap:8px}
.payments span{width:40px;height:22px;border-radius:3px;background:var(--white);opacity:.9}
</style>
</head>
<body>
<div class="page">

<header class="site-header">
  <div class="brand"><span class="brand-dot"></span>VEXAWATCH</div>
  <nav class="main-nav">
    <a href="#">HOME</a><a href="#">WHO WE ARE</a><a href="#">WHAT WE DO</a><a href="#">NEWS</a><a href="#">BLOG</a><a href="#">CONTACT US</a>
    <a href="#" class="login">MEMBER LOG IN</a>
  </nav>
</header>

<section class="hero">
  <div class="hero-copy">
    <h1>VEXAWATCH</h1>
    <ul class="hero-list">
      <li><svg width="14" height="14" viewBox="0 0 14 14"><circle cx="7" cy="7" r="7" fill="#fff"/><path d="M3.5 7.2l2.3 2.2 4.6-4.8" stroke="#0592cd" stroke-width="1.8" fill="none"/></svg>Vestibulum ante ipsum primis in faucibus orci luctus</li>
      <li><svg width="14" height="14" viewBox="0 0 14 14"><circle cx="7" cy="7" r="7" fill="#fff"/><path d="M3.5 7.2l2.3 2.2 4.6-4.8" stroke="#0592cd" stroke-width="1.8" fill="none"/></svg>Aenean a nibh eget turpis vehicula tempus ac sed massa.</li>
    </ul>
    <span class="hero-cta">From £15.99/month</span>
  </div>
  <div class="hero-media" role="img" aria-label="Laptop showing a smiling young woman using her computer"></div>
  <div class="slider-dots"><span></span><span></span><span></span><span></span></div>
</section>

<section class="welcome">
  <h2 class="section-title">WELCOME TO VEXAWATCH</h2>
  <p>We are passionate about keeping our members protected online, in a world where personal details are shared, stored and traded every day. Our team monitors thousands of sources so you can spot trouble early and act fast. From weekly reports to instant alerts, we help you stay one step ahead of fraudsters and keep your identity where it belongs — with you.</p>
</section>

<section class="split">
  <div class="split-col">
    <h2 class="section-title">WHAT WE DO</h2>
    <div class="what-body">
      <div class="what-media" role="img" aria-label="Hand touching a glowing digital security screen"></div>
      <div>
        <p class="small-text">Aliquam molestie, mi at imperdiet euismod, purus auctor tellus, at tincidunt lacus lectus in erat. Sed accumsan sollicitudin sapien, ac porta odio.</p>
      </div>
    </div>
    <span class="btn-small">READ MORE</span>
  </div>
  <div class="split-col">
    <h2 class="section-title">LATEST NEWS</h2>
    <div class="news-item"><p class="small-text">Aliquam molestie, mi at imperdiet euismod, dui purus auctor tellus, at tincidunt lacus lectus in erat.</p><span class="read">Read More</span></div>
    <div class="news-item"><p class="small-text">Aliquam molestie, mi at imperdiet euismod, dui purus auctor tellus, at tincidunt lacus lectus in erat.</p><span class="read">Read More</span></div>
    <span class="btn-small">READ MORE</span>
  </div>
</section>

<section class="why">
  <h2 class="section-title">WHY CHOOSE VEXAWATCH</h2>
  <div class="features">
    <div class="feature">
      <div class="feature-box"><svg width="40" height="36" viewBox="0 0 40 36"><path d="M20 3L37 33H3Z" fill="none" stroke="#fff" stroke-width="3" stroke-linejoin="round"/><rect x="18.5" y="13" width="3" height="10" fill="#fff"/><rect x="18.5" y="26" width="3" height="3" fill="#fff"/></svg></div>
      <h3>IDENTITY FRAUD<br>ALERTS</h3>
    </div>
    <div class="feature">
      <div class="feature-box"><svg width="42" height="30" viewBox="0 0 42 30"><rect x="2" y="2" width="38" height="26" fill="none" stroke="#fff" stroke-width="3"/><path d="M2 2l19 15L40 2" fill="none" stroke="#fff" stroke-width="3"/></svg></div>
      <h3>WEEKLY IDENTITY REPORTS<br>BY EMAIL OR SMS</h3>
    </div>
    <div class="feature">
      <div class="feature-box"><svg width="42" height="34" viewBox="0 0 42 34"><rect x="2" y="8" width="32" height="24" fill="none" stroke="#fff" stroke-width="3"/><path d="M2 8l16 12L34 8" fill="none" stroke="#fff" stroke-width="3"/><circle cx="35" cy="7" r="6" fill="#fff"/></svg></div>
      <h3>WEEKLY SOCIAL REPORTS<br>BY EMAIL OR SMS</h3>
    </div>
    <div class="feature">
      <div class="feature-box"><svg width="40" height="40" viewBox="0 0 40 40"><path d="M12 8c-3 0-5 3-4 6 3 9 9 15 18 18 3 1 6-1 6-4l-5-4-4 2c-3-2-5-4-7-7l2-4z" fill="#fff"/><circle cx="20" cy="20" r="17" fill="none" stroke="#fff" stroke-width="3"/><path d="M8 8l24 24" stroke="#fff" stroke-width="3"/></svg></div>
      <h3>STOP TELEMARKETING<br>CALLS</h3>
    </div>
  </div>
</section>

<section class="signup">
  <h2 class="section-title">SIGN UP TODAY NOW</h2>
  <div class="signup-form">
    <div class="field">Name</div><div class="field">Last Name</div><div class="field">Email Address</div>
  </div>
  <span class="submit">SUBMIT NOW</span>
</section>

<footer class="site-footer">
  <p class="footer-copy">Copyright © 2015 · VEXAWATCH</p>
  <p class="footer-links">Terms &amp; Conditions | Privacy Policy | Opt Out</p>
  <p class="footer-terms">Terms &amp; Conditions: Vexawatch provides identity monitoring services only and is not a credit reference agency. Membership renews monthly until cancelled and may be cancelled at any time from your account. Alerts are based on information available to us and cannot guarantee that every misuse of your details will be detected. Please read our full terms and privacy policy before joining. All prices include VAT where applicable.</p>
  <div class="footer-bottom">
    <div class="social"><span></span><span></span><span></span><span></span></div>
    <div class="payments"><span></span><span></span><span></span><span></span><span></span></div>
  </div>
</footer>

</div>
</body>
</html>
```